ESPDT Flyer to promote our services in the KPR Event in Nashville, TN

Please use our website at www.brightsprout.example to get our color seem and details about our program to design a flyer. This is exclusively for our EPSDT service not clinics or optometry.
BSI Mission Statement
Orchard Partners, LLC, dba, "Bright Sprout" feels a strong sense of connection to entities whose mission is to improve the educational achievements of students. In a similar way, Bright Sprout is committed to improving the health of children by providing healthcare to students and in a school-based setting. We work to keep children healthy, ready to learn and in the classroom.
We believe that undiagnosed and untreated health problems can become barriers to a child's ability to learn. We believe that preventive health services, in the school setting, reduce or eliminate barriers to healthcare. We believe that diversity is to be valued and respected.
It is Bright Sprout's desire provide the Annual health exams / Sports physicals and Optometry services to your students.
Description of Services
Annual Health Screening
These annual screenings and sports physicals will comply with the Early Periodic Screening, Diagnosis and Treatment (EPSDT) as mandated by the Tennessee Medicaid program. The intent of the EPSDT program is to identify problems at birth (Early), to check health status at different intervals (Periodic), provide services that will identify health issues (Screening) that lead to classification of health issues (Diagnosis and follow-up), and elimination or provide ongoing care for diagnosed health problems (Treatment).
Bright Sprout transports a portable and well-equipped clinic to each school site. Bright Sprout's practitioners diagnose medical illnesses and make referrals to the child’s primary care provider (PCP). The clinical teams consist of a Nurse Practitioner and three support team members.
This service is at No out-of-pocket Cost to the school district or parent. We bill insurances.
Target Market(s)
Coordinated School Healthcare Professinals
Industry/Entity Type
Health And Wellness
Requirements
Must have
- Must have description of the EPSDT exam
Nice to have
- Picture of diversity: Children and Nurses

```html
<!DOCTYPE html>
<html lang="en">
<head>
<meta charset="utf-8">
<title>Bright Sprout – EPSDT Services Flyer</title>
<link rel="stylesheet" href="https://fonts.googleapis.com/css2?family=Roboto+Condensed:wght@300;400;700&family=Great+Vibes&display=swap">
<style>
  :root{
    --blue:#1b5fab;
    --blue-deep:#0e4688;
    --blue-light:#3f86cf;
    --link:#2f6cb5;
    --ink:#3a3a3a;
    --paper:#ffffff;
    --dot:#9a9a9a;
  }
  *{margin:0;padding:0;box-sizing:border-box}
  html,body{width:930px;height:1200px;overflow:hidden;background:var(--paper)}
  body{font-family:"Roboto Condensed",Arial,sans-serif;font-weight:300;color:var(--ink);position:relative}
  .flyer{position:absolute;inset:0;background:linear-gradient(180deg,#fff 0%,#fff 55%,#eef3f9 85%,#fff 100%)}

  .photo{position:absolute;top:24px;height:186px;border:4px solid #fff;box-shadow:0 1px 4px rgba(0,0,0,.25)}
  .photo--family{left:48px;width:216px;background:linear-gradient(135deg,#c9b7a3,#7a5a45 55%,#e9e1d6)}
  .photo--kids{left:356px;width:216px;background:linear-gradient(160deg,#8ec6e8,#e8a64a 50%,#f2d54a 80%,#5aa24a)}
  .photo--nurse{left:674px;width:210px;background:linear-gradient(135deg,#9fb5c9,#2d3f66 55%,#d9c8b8)}

  .band{position:absolute;top:210px;height:52px;background:linear-gradient(180deg,var(--blue-light),var(--blue-deep));color:#fff;font-weight:700;font-size:16.5px;line-height:19px;text-align:center;display:flex;align-items:center;justify-content:center;text-transform:uppercase;letter-spacing:.2px}
  .band--parent{left:26px;width:250px}
  .band--exams{left:320px;width:284px}
  .band--assess{left:649px;width:250px}
  .fold{position:absolute;top:190px;width:20px;height:20px}

  .rule{position:absolute;top:248px;height:620px;border-left:3px dotted var(--dot)}
  .rule--a{left:290px}
  .rule--b{left:631px}

  .col{position:absolute;font-size:14.2px;line-height:16.4px}
  .col--parent{left:32px;top:274px;width:240px}
  .col--exams{left:304px;top:274px;width:314px;font-size:14.2px;line-height:18px}
  .col--assess{left:642px;top:274px;width:260px}

  .num{display:flex;margin-top:9px}
  .checks{list-style:none}
  .checks li{display:flex}
  .num span:first-child{width:18px;flex:none}
  .checks li::before{content:"✓";color:var(--blue);font-weight:700;width:18px;flex:none;font-size:15px}

  .lead{color:var(--link);font-weight:400;font-size:14.6px;margin:8px 0 0}
  .link{color:var(--link);text-decoration:underline}
  .col--exams p{margin-bottom:10px}

  .packet{padding-left:22px}
  .letters{list-style:none}
  .letters li{display:flex}
  .letters li span:first-child{width:18px;flex:none}
  .pa-title{color:var(--blue);font-weight:700;font-size:15.5px;text-align:center;margin:10px 0 10px;padding-right:10px}
  .pa-grid{display:grid;grid-template-columns:132px 1fr;list-style:none;grid-auto-flow:column;grid-template-rows:repeat(9,16.4px)}
  .pa-grid li{display:flex;white-space:nowrap}
  .pa-grid li span:first-child{width:18px;flex:none}
  .block{padding-left:7px;margin-top:12px;width:250px}
  .block p{margin-bottom:9px}
  .fine{font-size:8.4px;line-height:10px;padding-left:5px;width:200px;color:#333;font-weight:400}

  .brand{position:absolute;left:290px;top:878px;width:340px;text-align:center;color:var(--blue)}
  .brand .url{font-weight:700;font-size:18px}
  .brand .name{display:flex;align-items:center;justify-content:center;gap:12px;margin-top:14px;font-weight:700;font-size:44px;line-height:46px}
  .brand .dotmark{width:34px;height:34px;border-radius:50%;background:var(--blue);flex:none}
  .brand .tag{font-weight:400;font-size:14px;margin-top:4px;padding-left:40px}

  .wave{position:absolute;left:0;top:996px;width:930px;height:204px}
  .boy{position:absolute;left:0;top:872px;width:208px;height:328px;border-radius:90px 90px 0 0;background:linear-gradient(180deg,#b08560 0%,#d7a67e 40%,#3a6fb2 62%,#2c5c9c 100%)}

  .mission{position:absolute;left:216px;top:1020px;width:700px;color:#fff;font-size:12.4px;line-height:16.4px}
  .mission h2{font-family:"Great Vibes",cursive;font-weight:400;font-size:30px;line-height:34px;margin-left:100px;margin-bottom:4px}
  .beliefs{display:flex;list-style:none;margin-top:12px;gap:12px}
  .beliefs li{display:flex}
  .beliefs li span:first-child{width:18px;flex:none}
  .mission .closing{margin-top:14px;text-align:center;margin-left:-20px}
</style>
</head>
<body>
<div class="flyer">

  <div class="photo photo--family" role="img" aria-label="Photo of a smiling family of four sharing popcorn on a couch"></div>
  <div class="photo photo--kids" role="img" aria-label="Photo of a diverse group of smiling school children"></div>
  <div class="photo photo--nurse" role="img" aria-label="Photo of a nurse taking a young boy's blood pressure"></div>

  <svg class="fold" style="left:26px" viewBox="0 0 20 20"><polygon points="0,20 20,0 20,20" fill="var(--blue-deep)"/></svg>
  <svg class="fold" style="left:320px" viewBox="0 0 20 20"><polygon points="0,20 20,0 20,20" fill="var(--blue-deep)"/></svg>
  <svg class="fold" style="left:649px" viewBox="0 0 20 20"><polygon points="0,20 20,0 20,20" fill="var(--blue-deep)"/></svg>

  <h1 class="band band--parent">Parent / Guardian<br>Information</h1>
  <h1 class="band band--exams">Annual Health Exams /<br>Sports Physicals (EPSDT)</h1>
  <h1 class="band band--assess">Assessments &amp; Standards<br>of Documentation</h1>

  <div class="rule rule--a"></div>
  <div class="rule rule--b"></div>

  <section class="col col--parent">
    <div>All parents will receive the following:</div>
    <div class="num" style="margin-top:0"><span>1.</span><span>Parent Packet Consent/registration</span></div>
    <ul class="checks">
      <li>EPSDT Physical&nbsp; Early Pediatric Exam</li>
      <li>PEDS Pediatric Evaluation Developmental Screen</li>
      <li>Vision Exams</li>
      <li>Fluoride Exams for four (4) &amp; five (5) year olds</li>
    </ul>
    <div class="num"><span>2.</span><span>Exam Result forms sent on appropriate referrals</span></div>
    <ul class="checks">
      <li>EPSDT Results</li>
      <li>PEDS/Developmental Results</li>
      <li>Vision Referral</li>
      <li>Hearing Referral</li>
      <li>Mental Health Referral Letter</li>
      <li>Referral Follow-Up letter sent on all vision, hearing and PCP referrals</li>
    </ul>
    <div class="num"><span>3.</span><span>Possible Anticipatory Guidance or Health teaching forms</span></div>
    <ul class="checks">
      <li>Asthma</li>
      <li>Allergies</li>
      <li>Ear Cleaning</li>
      <li>Healthy Weight for your Child</li>
      <li>What Foods Give You Iron</li>
      <li>Why it is important to drink water</li>
      <li>Cholesterol</li>
      <li>Constipation</li>
      <li>Bike and Helmet Safety</li>
      <li>Screen Time</li>
      <li>Atopic Dermatitis/Eczema</li>
      <li>What is Tinea Capitis</li>
      <li>Smoking in the Home and the Impact on Children</li>
      <li>Where to get a Free Smoke Detector</li>
      <li>Breast Self Exam</li>
    </ul>
  </section>

  <section class="col col--exams">
    <p>It is Bright Sprout's desire to evaluate children and provide annual health exams / sports physicals to your students.</p>
    <div class="lead">DESCRIPTION OF SERVICES</div>
    <p><span class="link">Annual Health Screening</span>: These annual screenings and sports physicals will comply with the Early Periodic Screening, Diagnosis and Treatment (EPSDT) as mandated by the Tennessee Medicaid program.&nbsp; The intent of our EPSDT program is to identify problems pre-K through 12th grade, to check health status at different intervals (Periodic), provide services that will identify health issues (Screening) that lead to classification of health issues (Diagnosis and follow-up), and elimination or provide ongoing care for behavioral diagnosed health problems (Treatment).</p>
    <p>Our practitioners diagnose medical illnesses and make referrals to the child's primary care provider(PCP). The clinical teams consist of a Nurse Practitioner and two - three support team members.</p>
  </section>

  <section class="col col--assess">
    <div class="packet">
      <div>Parent Packet/Consent/Registration:</div>
      <ul class="letters">
        <li><span>a)</span><span>Medical History</span></li>
        <li><span>b)</span><span>Dietary History</span></li>
        <li><span>c)</span><span>PEDS Pediatric Evaluation<br>Development Screen</span></li>
        <li><span>d)</span><span>PEDS-DM</span></li>
        <li><span>e)</span><span>PSC Pediatric Symptom Checklist<br>up to age eight (8)</span></li>
        <li><span>f)</span><span>Sleep History</span></li>
        <li><span>g)</span><span>Developmental History</span></li>
        <li><span>h)</span><span>Family History</span></li>
        <li><span>i)</span><span>Harlow Pediatric Symptom Checklist</span></li>
        <li><span>j)</span><span>Risk Assessment – TB</span></li>
      </ul>
    </div>
    <div class="pa-title">Physical Assessment</div>
    <ul class="pa-grid">
      <li><span>a)</span><span>General</span></li>
      <li><span>b)</span><span>Head</span></li>
      <li><span>c)</span><span>Neck</span></li>
      <li><span>d)</span><span>Eyes</span></li>
      <li><span>e)</span><span>Ears</span></li>
      <li><span>f)</span><span>Nose</span></li>
      <li><span>g)</span><span>Throat/mouth/teeth</span></li>
      <li><span>h)</span><span>Chest</span></li>
      <li><span>i)</span><span>Breast/tanner stage</span></li>
      <li><span>j)</span><span>Lungs</span></li>
      <li><span>k)</span><span>Heart</span></li>
      <li><span>l)</span><span>Abdomen</span></li>
      <li><span>m)</span><span>Femoral Pulses</span></li>
      <li><span>n)</span><span>Genitalia/tanner stage</span></li>
      <li><span>o)</span><span>Extremities</span></li>
      <li><span>p)</span><span>Spine</span></li>
      <li><span>q)</span><span>Skin</span></li>
      <li><span>r)</span><span>Neuro</span></li>
    </ul>
    <div class="block">
      <p><span class="link">Vital signs:</span> Height, Weight, Blood Pressure, Pulse, Body Mass, Body mass Index (BMI)</p>
      <p><span class="link">Vision Screening:</span> Refracts the eye, detection of Amblyopia, Depth perception.&nbsp; No response is needed from the child.&nbsp; Color Blindness is tested on boys through second (2nd) grade.</p>
      <p><span class="link">Hearing Screening:</span> Tonal TX20 Headphones</p>
      <p>Lab work competed by age, risk assessment, or clinical findings:</p>
      <p>Urine testing, Hemoglobin/hematocrit testing for identifying anemia</p>
    </div>
    <div class="fine">This service is also at NO out-of-pocket cost to the school, district, or parent. The insurance companies are billed for these services.</div>
  </section>

  <div class="brand">
    <div class="url">www.brightsprout.example</div>
    <div class="name"><span class="dotmark"></span><span>Bright Sprout</span></div>
    <div class="tag">Innovators in School Health Care Services</div>
  </div>

  <svg class="wave" viewBox="0 0 930 204" preserveAspectRatio="none">
    <defs>
      <linearGradient id="waveFill" x1="0" y1="0" x2="1" y2="1">
        <stop offset="0" stop-color="#2a74c4"/>
        <stop offset="0.6" stop-color="#1a5aa6"/>
        <stop offset="1" stop-color="#0e4688"/>
      </linearGradient>
    </defs>
    <path d="M0,60 C260,-10 620,-10 930,40 L930,204 L0,204 Z" fill="url(#waveFill)"/>
  </svg>

  <div class="boy" role="img" aria-label="Photo of a smiling boy giving two thumbs up"></div>

  <section class="mission">
    <h2>Our Mission Statement</h2>
    <p>BSI Orchard Partners, LLC, dba, "Bright Sprout", feels a strong sense of connection to entities whose mission is to improve the educational achievements of students.&nbsp; In a similar way, Bright Sprout is committed to improving the health of children by providing healthcare to students in a school-based setting.&nbsp; We work to keep children healthy, ready to learn and in the classroom. We believe that:</p>
    <ul class="beliefs">
      <li style="width:250px"><span>a)</span><span>Undiagnosed and untreated health problems are barriers to a child's ability to learn.</span></li>
      <li style="width:270px"><span>b)</span><span>Preventive health services, provided in the school settings, reduce or eliminate barriers to healthcare.</span></li>
      <li style="width:150px"><span>c)</span><span>That diversity is to be valued and respected.</span></li>
    </ul>
    <p class="closing">It is Bright Sprout's desire to evaluate children and provide annual health exams / sports physicals to your students.</p>
  </section>

</div>
</body>
</html>
```